Restaurant needs a vertical banner for fried catfish

Our restaurant is looking for an eye-catching 78.75in. x 36in. vertical physical banner ad for our fried catfish. Photos for the fried catfish will be provided as a reference but we will also accept anything similar to the photo. We will be using the following as our receptacle: https://www.plankoria.example/banner-stand/retractable-banner-stands/
The design must incorporate the following flavor texts:
Fried Catfish
Always Fresh!
Made from Scratch
Hand-cut Fillets
The Best Catfish in Texas
Served with fries, hush puppies, and a 32oz fountain drink
Also available by the pound!
The final design should be creative, professional, and eye-catching for customers.
Updates
Colors
Designer to choose colors to be used in the design.
Requirements
Must have
- We are open to any and all design elements, albeit the 'flavor texts' should not overpower, but complement the fried catfish photo. 'Fried Catfish' can be used in lieu of a main title/logo.
Nice to have
- Transparent or textured backgrounds that can encompass any or all part of the banner such as a cutting board, shadows, abstract, etc to show depth are a plus.
- Use of vectors or objects such as ribbons or shapes to encapsulate the 'flavor texts' are also encouraged.

```html
<!DOCTYPE html>
<html lang="en">
<head>
<meta charset="utf-8">
<title>Fried Catfish Vertical Banner</title>
<link rel="stylesheet" href="https://fonts.googleapis.com/css2?family=Fira+Sans:wght@800&family=Comic+Neue:wght@700&family=Kalam:wght@400&display=swap">
<style>
  :root {
    --page: #dedbd8;
    --board: #232323;
    --board-light: #2e2e2e;
    --gold: #f0a00a;
    --red: #f50a0a;
    --orange: #ff6a0a;
    --white: #ffffff;
  }
  * { margin: 0; padding: 0; box-sizing: border-box; }
  html, body { width: 1200px; height: 842px; overflow: hidden; }
  body { background: var(--page); position: relative; }

  .banner {
    position: absolute;
    left: 420px;
    top: 27px;
    width: 360px;
    height: 788px;
    overflow: hidden;
    background:
      repeating-linear-gradient(92deg, rgba(255,255,255,0.025) 0 2px, transparent 2px 7px),
      radial-gradient(ellipse at 50% 40%, var(--board-light), var(--board) 75%);
  }
  .awning { position: absolute; left: 0; top: 0; width: 360px; height: 70px; display: block; }

  .title {
    position: absolute; left: 0; width: 100%; top: 94px;
    text-align: center;
    font-family: "Fira Sans", sans-serif; font-weight: 800;
    font-size: 45px; line-height: 1; letter-spacing: 1px; color: var(--gold);
  }
  .tagline {
    position: absolute; left: 0; width: 100%; top: 141px;
    text-align: center;
    font-family: "Kalam", cursive; font-size: 25px; line-height: 1.2; color: var(--white);
  }

  .dish-photo {
    position: absolute; left: 43px; top: 186px;
    width: 274px; height: 274px; border-radius: 50%;
    border: 2px solid var(--white);
    background:
      radial-gradient(circle at 62% 14%, #d94a2a 0 9%, transparent 10%),
      radial-gradient(circle at 30% 78%, #e8b64a 0 22%, transparent 40%),
      radial-gradient(circle at 58% 48%, #b5701e 0 30%, #8c5116 55%, #f1e9da 80%);
  }

  .feature { position: absolute; height: 46px; }
  .feature svg { position: absolute; inset: 0; width: 100%; height: 100%; }
  .feature span {
    position: relative; display: block; line-height: 46px; text-align: center;
    font-family: "Comic Neue", cursive; font-weight: 700; font-size: 20px;
    color: var(--white); letter-spacing: 0.5px;
  }
  .feature-scratch { left: 60px; top: 476px; width: 268px; }
  .feature-fillets { left: 58px; top: 533px; width: 252px; }
  .feature-best    { left: 46px; top: 589px; width: 274px; }
  .feature-scratch span { padding-right: 52px; }
  .feature-fillets span { padding-right: 38px; }
  .feature-best span { padding-right: 4px; }

  .served {
    position: absolute; left: 0; width: 100%; top: 648px;
    text-align: center;
    font-family: "Kalam", cursive; font-size: 14.5px; line-height: 20px;
    color: var(--white);
  }

  .by-pound { position: absolute; left: 0; bottom: 0; width: 360px; height: 72px; }
  .by-pound svg { position: absolute; inset: 0; width: 100%; height: 100%; }
  .by-pound p {
    position: absolute; left: 0; width: 100%; top: 30px;
    text-align: center;
    font-family: "Comic Neue", cursive; font-weight: 700; font-size: 20px;
    color: var(--white);
  }
</style>
</head>
<body>
  <main class="banner">
    <svg class="awning" viewBox="0 0 360 70" aria-hidden="true">
      <g>
        <path fill="var(--red)" d="M0 0H22.5V58A11.25 11.25 0 0 1 0 58Z"/>
        <path fill="var(--gold)" d="M22.5 0H45V58A11.25 11.25 0 0 1 22.5 58Z"/>
        <path fill="var(--red)" d="M45 0H67.5V58A11.25 11.25 0 0 1 45 58Z"/>
        <path fill="var(--gold)" d="M67.5 0H90V58A11.25 11.25 0 0 1 67.5 58Z"/>
        <path fill="var(--red)" d="M90 0H112.5V58A11.25 11.25 0 0 1 90 58Z"/>
        <path fill="var(--gold)" d="M112.5 0H135V58A11.25 11.25 0 0 1 112.5 58Z"/>
        <path fill="var(--red)" d="M135 0H157.5V58A11.25 11.25 0 0 1 135 58Z"/>
        <path fill="var(--gold)" d="M157.5 0H180V58A11.25 11.25 0 0 1 157.5 58Z"/>
        <path fill="var(--red)" d="M180 0H202.5V58A11.25 11.25 0 0 1 180 58Z"/>
        <path fill="var(--gold)" d="M202.5 0H225V58A11.25 11.25 0 0 1 202.5 58Z"/>
        <path fill="var(--red)" d="M225 0H247.5V58A11.25 11.25 0 0 1 225 58Z"/>
        <path fill="var(--gold)" d="M247.5 0H270V58A11.25 11.25 0 0 1 247.5 58Z"/>
        <path fill="var(--red)" d="M270 0H292.5V58A11.25 11.25 0 0 1 270 58Z"/>
        <path fill="var(--gold)" d="M292.5 0H315V58A11.25 11.25 0 0 1 292.5 58Z"/>
        <path fill="var(--red)" d="M315 0H337.5V58A11.25 11.25 0 0 1 315 58Z"/>
        <path fill="var(--gold)" d="M337.5 0H360V58A11.25 11.25 0 0 1 337.5 58Z"/>
      </g>
    </svg>

    <h1 class="title">FRIED CATFISH</h1>
    <p class="tagline">ALWAYS FRESH!</p>

    <div class="dish-photo" role="img" aria-label="Plate of golden cornmeal-crusted fried catfish fillets with fries, hush puppies and tomato"></div>

    <div class="feature feature-scratch">
      <svg viewBox="0 0 300 50" preserveAspectRatio="none" aria-hidden="true">
        <g fill="var(--gold)">
          <path d="M10 9 C70 5 150 6 215 7 C226 13 223 40 212 44 C150 46 70 47 14 45 C4 40 2 32 6 26 C3 20 4 13 10 9 Z"/>
          <path d="M196 5 L294 2 L291 5 L200 8 Z"/>
          <path d="M208 11 L282 10 L277 13 L210 14 Z"/>
          <path d="M212 17 L298 16 L293 19 L212 21 Z"/>
          <path d="M214 23 L268 22 L266 25 L213 27 Z"/>
          <path d="M213 29 L290 28 L285 31 L212 33 Z"/>
          <path d="M211 35 L260 35 L257 38 L210 39 Z"/>
          <path d="M200 41 L252 42 L246 45 L198 46 Z"/>
          <path d="M30 46 L120 46 L110 49 L36 49 Z"/>
        </g>
      </svg>
      <span>Made from Scratch</span>
    </div>

    <div class="feature feature-fillets">
      <svg viewBox="0 0 300 50" preserveAspectRatio="none" aria-hidden="true">
        <g fill="var(--red)">
          <path d="M12 8 C80 4 170 5 236 6 C248 12 246 40 234 44 C160 47 80 47 16 45 C5 41 2 33 6 26 C2 19 5 12 12 8 Z"/>
          <path d="M160 3 L262 2 L258 5 L166 6 Z"/>
          <path d="M232 12 L296 11 L290 14 L232 16 Z"/>
          <path d="M234 20 L274 19 L271 22 L234 24 Z"/>
          <path d="M233 28 L292 28 L286 31 L232 32 Z"/>
          <path d="M230 37 L270 37 L266 40 L229 41 Z"/>
        </g>
      </svg>
      <span>Hand-cut Fillets</span>
    </div>

    <div class="feature feature-best">
      <svg viewBox="0 0 300 50" preserveAspectRatio="none" aria-hidden="true">
        <g fill="var(--orange)">
          <path d="M16 9 C90 5 190 6 272 8 C292 10 298 22 296 30 C294 40 284 44 268 45 C190 47 90 47 18 45 C6 42 2 34 5 27 C3 19 7 12 16 9 Z"/>
          <path d="M60 4 L200 2 L195 5 L64 7 Z"/>
          <path d="M170 0.5 L262 1 L255 3.5 L172 3.5 Z"/>
          <path d="M40 46 L170 47 L160 49.5 L46 49.5 Z"/>
        </g>
      </svg>
      <span>The Best Catfish in Texas</span>
    </div>

    <p class="served">Served with fries, hush puppies,<br>and a 32oz fountain drink</p>

    <div class="by-pound">
      <svg viewBox="0 0 360 72" preserveAspectRatio="none" aria-hidden="true">
        <g fill="var(--gold)">
          <path d="M0 22 C60 18 120 16 170 13 C230 11 300 10 360 12 L360 72 L0 72 Z"/>
          <path d="M120 10 L250 7 L246 10 L126 12 Z"/>
          <path d="M170 4 L300 3 L296 6 L176 7 Z"/>
          <path d="M260 0 L350 0.5 L344 3 L264 3 Z"/>
          <path d="M60 16 L140 14 L134 17 L64 18 Z"/>
          <path d="M320 44 L360 43 L360 46 L326 47 Z"/>
        </g>
      </svg>
      <p>Also available by the pound!</p>
    </div>
  </main>
</body>
</html>
```